Harbor Lantern Security Solutions Business Cards

We are looking for a "catchy" business card that contains blue and red as well as incorporating our logo design. Gold is also an option. Anything that stands out and looks awesome!!! The final design should communicate security and trust.
We are advertising home security systems with monitoring services, video surveillance as well as custom gates with key pad entry.

Website address: www.bluecrestwardtx.example
Phone number: 555-555-0193
Owner: Marcus Orlend
Located in Maple Ridge, Westmarch
License Number: K47315
Licensed and Insured
Logo: We're There When You're Not

I'm not sure if all of this is needed, but just in case!!!

Target Market(s)

Commercial and Residential

Industry/Entity Type

Business

Contact Information for Business Card

Owner: Marcus Orlend
Email Address: morlend@mailbeam.example

Font styles to use
Sans Serif

Colors
ec1f27
fbed22
0355a3

Requirements
Must have
• Residential and Commercial Alarm Systems, Monitoring Services. Video Surveillance, Custom Gates and Key Pad Entry
Nice to have
• Everything would be nice although I don't want the card to look overcrowded.

```html
<!DOCTYPE html>
<html lang="en">
<head>
<meta charset="utf-8">
<title>Harbor Lantern Security Solutions – Business Cards</title>
<link rel="stylesheet" href="https://fonts.googleapis.com/css2?family=Montserrat:wght@400;500;700&display=swap">
<style>
  :root{
    --navy:#1d4f7e;
    --blue-light:#3b8cc4;
    --red:#e0332e;
    --paper:#f4f4f4;
    --white:#ffffff;
    --backdrop:#d9dbde;
    --ink-brand:#1f4f82;
  }
  *{box-sizing:border-box;margin:0;padding:0}
  html,body{width:1200px;height:800px;overflow:hidden}
  body{
    background:var(--backdrop);
    font-family:"Montserrat",sans-serif;
    display:flex;align-items:center;justify-content:center;gap:40px;
  }
  .card{
    position:relative;width:560px;height:320px;overflow:hidden;
    box-shadow:0 10px 30px rgba(0,0,0,.18);
  }
  .card-art{position:absolute;inset:0;width:100%;height:100%}
  .brand{position:absolute;display:flex;align-items:center;gap:14px}
  .brand-dot{width:62px;height:62px;border-radius:50%;background:var(--red);flex:none}
  .brand-name{
    font-weight:700;font-size:15px;line-height:1.25;color:var(--ink-brand);
    text-transform:uppercase;letter-spacing:.06em;width:170px;
  }

  /* front */
  .card-front{background:var(--paper)}
  .card-front .brand{top:24px;right:34px}
  .owner{position:absolute;left:34px;top:150px;color:var(--white)}
  .owner-name{font-weight:500;font-size:30px;letter-spacing:.01em}
  .owner-title{font-weight:400;font-size:13px;letter-spacing:.12em;margin-top:2px}
  .contact-list{
    position:absolute;left:34px;top:226px;list-style:none;color:var(--white);
    font-size:11px;line-height:1.6;
  }
  .contact-list li{display:flex;align-items:center;gap:9px}
  .contact-list svg{width:11px;height:11px;flex:none}

  /* back */
  .card-back{background:var(--navy)}
  .card-back .brand{left:30px;top:128px;flex-direction:column;align-items:flex-start;gap:10px}
  .services{
    position:absolute;right:30px;top:60px;text-align:right;list-style:none;
    color:var(--white);font-size:13px;line-height:1.55;
  }
  .services li::after{content:"";display:inline-block;width:5px;height:5px;border-radius:50%;background:var(--white);margin-left:9px;vertical-align:middle}
  .services .services-lead{font-weight:700;letter-spacing:.02em}
  .services .services-lead::after{display:none}
  .license{
    position:absolute;right:30px;bottom:28px;text-align:right;color:var(--white);
    font-size:11px;line-height:1.5;
  }
</style>
</head>
<body>

  <section class="card card-front" aria-label="Business card front">
    <svg class="card-art" viewBox="0 0 560 320" preserveAspectRatio="none" aria-hidden="true">
      <path d="M0,122 C120,80 230,72 300,120 C370,168 420,240 560,232 L560,320 L0,320 Z" fill="var(--blue-light)"/>
      <path d="M0,130 C120,90 225,84 292,130 C362,178 415,254 560,246 L560,320 L0,320 Z" fill="var(--navy)"/>
    </svg>
    <div class="brand">
      <span class="brand-dot"></span>
      <span class="brand-name">Harbor Lantern Security Solutions</span>
    </div>
    <div class="owner">
      <p class="owner-name">Marcus Orlend</p>
      <p class="owner-title">OWNER</p>
    </div>
    <ul class="contact-list">
      <li><svg viewBox="0 0 12 12"><rect x="3" y="0.5" width="6" height="11" rx="1.2" fill="none" stroke="#fff" stroke-width="1.2"/><line x1="5" y1="9.5" x2="7" y2="9.5" stroke="#fff"/></svg>555 - 555 - 0193</li>
      <li><svg viewBox="0 0 12 12"><rect x="0.6" y="2" width="10.8" height="8" fill="none" stroke="#fff" stroke-width="1.2"/><path d="M0.6,2 L6,6.5 L11.4,2" fill="none" stroke="#fff" stroke-width="1.2"/></svg>morlend@mailbeam.example</li>
      <li><svg viewBox="0 0 12 12"><circle cx="6" cy="6" r="5.2" fill="none" stroke="#fff" stroke-width="1.1"/><ellipse cx="6" cy="6" rx="2.3" ry="5.2" fill="none" stroke="#fff" stroke-width="1"/><line x1="0.8" y1="6" x2="11.2" y2="6" stroke="#fff"/></svg>www.bluecrestwardtx.example</li>
      <li><svg viewBox="0 0 12 12"><path d="M6,11.5 C3,8 2,6.2 2,4.5 A4,4 0 0 1 10,4.5 C10,6.2 9,8 6,11.5 Z" fill="#fff"/><circle cx="6" cy="4.5" r="1.4" fill="var(--navy)"/></svg>Maple Ridge, Westmarch</li>
    </ul>
  </section>

  <section class="card card-back" aria-label="Business card back">
    <svg class="card-art" viewBox="0 0 560 320" preserveAspectRatio="none" aria-hidden="true">
      <path d="M0,0 L300,0 C230,40 225,110 250,170 C280,240 280,290 230,320 L0,320 Z" fill="var(--blue-light)"/>
      <path d="M0,0 L288,0 C218,40 213,110 238,170 C268,240 268,290 218,320 L0,320 Z" fill="var(--paper)"/>
    </svg>
    <div class="brand">
      <span class="brand-dot"></span>
      <span class="brand-name">Harbor Lantern Security Solutions</span>
    </div>
    <ul class="services">
      <li class="services-lead">Residential and Commercial</li>
      <li>Alarm Systems</li>
      <li>Monitoring Services</li>
      <li>Video Surveillance</li>
      <li>Custom Gates</li>
      <li>Key Pad Entry</li>
    </ul>
    <p class="license">Licensed and Insured<br>License Number: K47315</p>
  </section>

</body>
</html>
```